Business Cards

Need business card design that I can update for new employees and details. Needs to incorporate our logo, be bright and fun (in line with tourism and holidays)
Would like a Map of Western Australia on the front with locations all the caravan parks we own (just purchased Tom Price so please include that as well as others listed on our website).
Target Market(s)
Famillies
Contact Information for Business Card
5 Cards -
Mark Pettigrew (Director) e: pettigrew@bluewattle.com.au p: 0462 318 904
Lucy Pettigrew (Director) e: pettigrew@bluewattle.com.au p: 0455 896 320
Peter Halvorsen (General Manager) e: halvorsen@bluewattle.com.au p: 0471 552 648
Mina Halvorsen (General Manager) e: halvorsen@bluewattle.com.au p: 0471 552 649
Neil Whitcombe (Training and Operations Manager) - e: whitcombe@bluewattle.com.au p:0427 160 493
Colors
Designer to choose colors to be used in the design.
Look and feel
Each slider illustrates characteristics of the customer's brand and the style your logo design should communicate.

```html
<!DOCTYPE html>
<html lang="en">
<head>
<meta charset="utf-8">
<title>Bluewattle Tourist Parks – Business Card</title>
<link rel="stylesheet" href="https://fonts.googleapis.com/css2?family=Libre+Baskerville:wght@400;700&display=swap">
<style>
  :root {
    --backdrop: #ece9e4;
    --card-white: #fbfbfb;
    --teal-light: #9ad6cd;
    --teal: #7cc4ba;
    --teal-deep: #5fa89f;
    --brand-grey: #6f6f6f;
    --ink-white: #ffffff;
    --shadow: rgba(40, 40, 40, 0.22);
  }
  * { box-sizing: border-box; margin: 0; padding: 0; }
  html, body {
    width: 1200px;
    height: 780px;
    overflow: hidden;
    background: var(--backdrop);
    font-family: "Libre Baskerville", "Times New Roman", serif;
  }
  .sheet {
    position: relative;
    width: 1200px;
    height: 780px;
  }
  .card {
    position: absolute;
    top: 231px;
    width: 520px;
    height: 318px;
    overflow: hidden;
    box-shadow: 0 10px 24px var(--shadow);
  }
  .card--front { left: 50px; background: var(--card-white); }
  .card--back {
    left: 630px;
    background: radial-gradient(ellipse at 55% 40%, var(--teal-light) 0%, var(--teal) 55%, var(--teal-deep) 100%);
  }
  .wave {
    position: absolute;
    inset: 0;
    width: 100%;
    height: 100%;
  }
  .brand {
    position: absolute;
    display: flex;
    align-items: center;
    gap: 14px;
  }
  .brand__square {
    width: 50px;
    height: 50px;
    flex: none;
  }
  .brand__name {
    font-weight: 400;
    font-variant: small-caps;
    letter-spacing: 0.16em;
    line-height: 1.25;
  }
  .brand__name span { display: block; }
  .brand__line-main { font-size: 26px; }
  .brand__line-sub { font-size: 12px; letter-spacing: 0.3em; }

  .card--front .brand { left: 34px; top: 96px; }
  .card--front .brand__square { background: var(--teal); }
  .card--front .brand__name { color: var(--brand-grey); }

  .card--back .brand { left: 50%; top: 50%; transform: translate(-50%, -50%); }
  .card--back .brand__square { border: 2px solid var(--ink-white); background: rgba(255,255,255,0.92); }
  .card--back .brand__name { color: var(--ink-white); }

  .contact {
    position: absolute;
    left: 252px;
    top: 214px;
    color: var(--ink-white);
  }
  .contact__name { font-size: 17px; font-weight: 700; }
  .contact__role { font-size: 11px; margin-top: 2px; }
  .contact__list { list-style: none; margin-top: 12px; }
  .contact__item {
    display: flex;
    align-items: center;
    gap: 8px;
    font-size: 12px;
    margin-top: 6px;
  }
  .contact__icon { width: 14px; height: 14px; flex: none; }
</style>
</head>
<body>
<main class="sheet">

  <section class="card card--front" aria-label="Business card front">
    <svg class="wave" viewBox="0 0 520 318" preserveAspectRatio="none" aria-hidden="true">
      <defs>
        <linearGradient id="waveFill" x1="0" y1="1" x2="1" y2="0">
          <stop offset="0" stop-color="#6fb9af"/>
          <stop offset="0.5" stop-color="#9ad6cd"/>
          <stop offset="1" stop-color="#7cc4ba"/>
        </linearGradient>
      </defs>
      <path d="M160 318 C175 265 200 225 240 200 C300 165 390 150 440 100 C470 70 485 30 495 0 L520 0 L520 318 Z" fill="url(#waveFill)"/>
    </svg>

    <div class="brand">
      <div class="brand__square"></div>
      <p class="brand__name">
        <span class="brand__line-main">Bluewattle</span>
        <span class="brand__line-sub">Tourist Parks</span>
      </p>
    </div>

    <div class="contact">
      <p class="contact__name">Mark Pettigrew</p>
      <p class="contact__role">Director</p>
      <ul class="contact__list">
        <li class="contact__item">
          <svg class="contact__icon" viewBox="0 0 14 14" aria-hidden="true">
            <circle cx="7" cy="7" r="6.3" fill="none" stroke="#fff" stroke-width="1"/>
            <rect x="4.8" y="3.4" width="4.4" height="7.2" rx="0.8" fill="none" stroke="#fff" stroke-width="1"/>
          </svg>
          <span>0462 318 904</span>
        </li>
        <li class="contact__item">
          <svg class="contact__icon" viewBox="0 0 14 14" aria-hidden="true">
            <circle cx="7" cy="7" r="6.3" fill="none" stroke="#fff" stroke-width="1"/>
            <rect x="3.6" y="4.6" width="6.8" height="4.8" fill="none" stroke="#fff" stroke-width="1"/>
            <path d="M3.6 4.6 L7 7.4 L10.4 4.6" fill="none" stroke="#fff" stroke-width="1"/>
          </svg>
          <span>pettigrew@bluewattle.com.au</span>
        </li>
      </ul>
    </div>
  </section>

  <section class="card card--back" aria-label="Business card back">
    <div class="brand">
      <div class="brand__square"></div>
      <p class="brand__name">
        <span class="brand__line-main">Bluewattle</span>
        <span class="brand__line-sub">Tourist Parks</span>
      </p>
    </div>
  </section>

</main>
</body>
</html>
```